依頼詳細
今回初めて募集させていただきます。

依頼は、月刊誌「青嶺」の裏表紙デザインをお願い致します。青嶺されている一般の方は、必ず目にする雑誌です。サイズは【左右154mm×天地232mm】です。尚、2015年10月号(10月1日発刊)に掲載予定です。

当社製品をメインに、シンプルかつ高級感のあるデザインを希望致します。
なんとなくあるイメージは、雑誌によく掲載されているハイブランドの広告のような物を想像していますが、それにとらわれず斬新なものでもかまいません。
ご参考に弊社ホームページをご覧下さい。

今回は「製品紹介」広告ではありませんので、あくまでも企業イメージの浸透をテーマに製作をお願い致します。

尚、写真は約3GB分、こちらの共有ボックス(http://mokubako.jp/box/8TrLw5)においています。添付資料として、弊社ロゴをepsにて、また、2013年に掲載した広告を載せておきます。

よろしくお願い致します。
記載項目
社名:有限会社 朝霧工芸製作所
住所:〒811-1348 福岡市南区桜台7-31-16
電話番号:092-555-3470
FAX:092-555-3475
URL:http://www.asagirikogei.com/
東洋工芸品連合会会員
弊社ロゴ
「初心者用から特註高級品まで」
「カケ」という漢字(常用漢字ではないです、添付の資料2013年9月の広告の中でご確認下さい)
希望イメージ
シンプル 複雑
単色 カラフル
暗い 明るい
日常 高級
遊び心 厳粛
未来的 伝統的
女性的 男性的
希望する色
設定なし
納品ファイル
• イラストレーター形式 (.ai)
補足説明
納品物は
・イラストレータデータ(アウトライン済)
・イラストレータデータ(アウトライン前)+使用しているフォント
いずれも、Adobe illustrator CS6 で編集可能な.aiファイルにてお願い致します。
尚、採用されたデザインの著作権などの権利は、当社に帰属するようにお願致します。
.tifファイルですが、ロゴを追加しました。
フォントの納品、およびアウトライン前のaiデータの納品は、事前に調整に応じていただければ納品しなくて大丈夫です。
本日までに予想をはるかに超える提案をいただいておりまして、なんとも甲乙つけがたしの作品がたくさんあります。

1つは当選作品を選ばせてもらいますが、なんとも惜しいランサーの方の作品に関しては、締め切り後このサイトの直接依頼という形で作品を買い取らせていただきたいと考えています。

買取価格は個別に提示させていただきますので、価格が折り合えばどうぞよろしくお願いいたします。
■ 選んだ理由

「ハイブランドのような」という弊社の思っていたデザインとぴったり一致しました。シンプルかつモノトーンでまとめられ、必要な文言はすべて入っておりまして、弊社職人集団としての力強さをも感じさせてくれました。

■ 提案者全員のお礼・コメント

今回は予想外の数の提案があり、秀逸なデザインばかりでした。誠に有難うございます。次回、傾向とサイズを変えて再び募集いたしますので、その時も是非ご参加をお待ちしています。

```html
<!DOCTYPE html>
<html lang="ja">
<head>
<meta charset="utf-8">
<title>朝霧工芸製作所 裏表紙広告</title>
<link href="https://fonts.googleapis.com/css2?family=Shippori+Mincho:wght@400;600;800&display=swap" rel="stylesheet">
<style>
  :root {
    --ground: #5a1631;
    --ground-deep: #3f0d22;
    --ink-light: #f4efe6;
    --ink-soft: #d9cfc4;
    --photo-olive: #8e8a5c;
    --photo-cream: #ece4d4;
    --photo-wood: #b89a72;
    --photo-wood-dark: #8a6c4a;
    --photo-navy: #2a2f55;
    --photo-red: #a0323f;
    --photo-shade: rgba(58, 14, 30, 0.88);
  }
  * { margin: 0; padding: 0; box-sizing: border-box; }
  html, body { width: 796px; height: 1200px; overflow: hidden; background: var(--ground-deep); }
  .poster {
    position: relative;
    width: 796px;
    height: 1200px;
    overflow: hidden;
    background: radial-gradient(ellipse at 30% 85%, var(--ground) 0%, var(--ground-deep) 85%);
    font-family: "Shippori Mincho", serif;
    color: var(--ink-light);
  }
  .photo { position: absolute; overflow: hidden; }
  .photo--grip-detail {
    left: 0; top: 0; width: 398px; height: 244px;
    border-bottom-left-radius: 200px 120px;
    background: linear-gradient(160deg, var(--photo-cream) 0%, var(--photo-olive) 55%, #5d5a3a 100%);
  }
  .photo--signed-box {
    left: 0; top: 254px; width: 398px; height: 344px;
    background: linear-gradient(100deg, var(--photo-wood) 0%, #cdb48e 45%, var(--photo-wood-dark) 100%);
  }
  .photo--glove-case {
    left: 0; top: 608px; width: 398px; height: 294px;
    border-bottom-left-radius: 300px 260px;
    background: linear-gradient(135deg, var(--photo-navy) 0%, #c9a97a 55%, var(--photo-red) 100%);
  }
  .photo--glove-main {
    left: 404px; top: 0; width: 392px; height: 770px;
    border-top-left-radius: 260px 300px;
    background:
      linear-gradient(90deg, transparent 0%, transparent 62%, var(--photo-shade) 76%, var(--photo-shade) 100%),
      linear-gradient(200deg, var(--photo-red) 0%, var(--photo-cream) 40%, #d8cdb9 75%, #6e2236 100%);
  }
  .tagline {
    position: absolute;
    left: 708px; top: 84px;
    writing-mode: vertical-rl;
    font-size: 15px;
    letter-spacing: 5px;
    color: var(--ink-light);
  }
  .kake-character {
    position: absolute;
    left: 500px; top: 800px;
    font-size: 340px;
    line-height: 1;
    font-weight: 400;
    color: var(--ink-light);
  }
  .company {
    position: absolute;
    left: 78px; top: 972px;
  }
  .company__type {
    display: block;
    margin-left: 92px;
    font-size: 17px;
    letter-spacing: 4px;
    color: var(--ink-light);
  }
  .company__name-row { display: flex; align-items: center; gap: 14px; margin-top: 4px; }
  .company__mark {
    width: 42px; height: 42px;
    border-radius: 50%;
    background: var(--ink-light);
    flex: none;
  }
  .company__name {
    font-size: 33px;
    font-weight: 600;
    letter-spacing: 1px;
    color: var(--ink-light);
    white-space: nowrap;
  }
  .company__membership {
    display: block;
    margin-top: 6px;
    margin-left: 170px;
    font-size: 11px;
    color: var(--ink-soft);
  }
  .contact {
    position: absolute;
    left: 92px; top: 1084px;
    font-size: 12px;
    font-style: normal;
    line-height: 1.7;
    color: var(--ink-soft);
    white-space: nowrap;
  }
  .contact span + span { margin-left: 16px; }
</style>
</head>
<body>
<main class="poster">
  <div class="photo photo--grip-detail" role="img" aria-label="刺繍入りのカケの手首部分の写真"></div>
  <div class="photo photo--signed-box" role="img" aria-label="職人の銘が書かれた桐箱とカケの写真"></div>
  <div class="photo photo--glove-case" role="img" aria-label="落款入りの紺色の袋とカケの写真"></div>
  <div class="photo photo--glove-main" role="img" aria-label="織物の手首が付いた白い鹿革のカケの写真"></div>

  <p class="tagline">初心者用から特註高級品まで</p>

  <p class="kake-character">弽</p>

  <section class="company">
    <span class="company__type">有限会社</span>
    <div class="company__name-row">
      <span class="company__mark"></span>
      <span class="company__name">朝霧工芸製作所</span>
    </div>
    <span class="company__membership">東洋工芸品連合会会員</span>
  </section>

  <address class="contact">
    <div><span>〒811-1348 福岡市南区桜台7-31-16</span><span>電話番号：092-555-3470</span></div>
    <div><span>FAX：092-555-3475</span><span>http://www.asagirikogei.com/</span></div>
  </address>
</main>
</body>
</html>
```